Business card on Pvc transparent frosted

I need a business advertising card that will be eye catching and fun.
Target Market(s)
Rednecks, country, hunters, Fisherman, ATV users, lifted trucks, cowboys, cattle ranchers, farmers, etc
Industry/Entity Type
Apparel Store
Contact Information for Business Card
This will he printed on single side of a transparent frosted plastic card with shinny foil print option.
Requirements
Must have
- 1 - My logo.
- 2 - HOLLER BOOTSTRAP OUTFITTERS
- 3 - my motto "DONT judge how we look..... Judge the WILD mess we make!!"; 4 - my website "hollerbootstrap@mailvex.example"

Nice to have
- Use your imagination with negative space, partial graffics, etc. Keep in mind you can kind of see through the card

Should not have
- Do not change colors of chevrons

```html
<!DOCTYPE html>
<html lang="en">
<head>
<meta charset="utf-8">
<title>Holler Bootstrap Outfitters – Business Card</title>
<link rel="stylesheet" href="https://fonts.googleapis.com/css2?family=Montserrat:wght@900&family=Lato:wght@400;700&display=swap">
<style>
  :root {
    --stage: #3a3b3e;
    --card-black: #060709;
    --accent-yellow: #f7d23e;
    --accent-red: #ed2224;
    --band-grey: #9d9d9d;
    --rule-white: #ffffff;
    --text-white: #ffffff;
  }
  html, body {
    margin: 0;
    width: 1200px;
    height: 900px;
    overflow: hidden;
    background: var(--stage);
  }
  .business-card {
    position: absolute;
    left: 100px;
    top: 164px;
    width: 1000px;
    height: 572px;
    border-radius: 44px;
    overflow: hidden;
    background: var(--card-black);
  }
  .card-shapes {
    position: absolute;
    inset: 0;
  }
  .brand-title {
    position: absolute;
    left: 150px;
    top: 62px;
    margin: 0;
    font-family: "Montserrat", sans-serif;
    font-weight: 900;
    font-size: 46px;
    letter-spacing: -1px;
    color: var(--accent-yellow);
    -webkit-text-stroke: 2px var(--accent-red);
    paint-order: stroke fill;
    white-space: nowrap;
  }
  .brand-mark {
    position: absolute;
    left: 360px;
    top: 200px;
    display: flex;
    align-items: center;
    gap: 14px;
  }
  .brand-mark-dot {
    width: 26px;
    height: 26px;
    border-radius: 50%;
    background: var(--accent-yellow);
  }
  .brand-mark-name {
    font-family: "Lato", sans-serif;
    font-weight: 700;
    font-size: 28px;
    color: var(--text-white);
    letter-spacing: 1px;
  }
  .website {
    position: absolute;
    right: 190px;
    top: 370px;
    margin: 0;
    font-family: "Lato", sans-serif;
    font-weight: 400;
    font-size: 32px;
    color: var(--text-white);
    letter-spacing: 0.5px;
    white-space: nowrap;
  }
  .motto {
    position: absolute;
    left: 50px;
    top: 508px;
    width: 760px;
    margin: 0;
    font-family: "Lato", sans-serif;
    font-weight: 400;
    font-size: 21px;
    color: var(--accent-red);
    white-space: nowrap;
  }
</style>
</head>
<body>
  <article class="business-card">
    <svg class="card-shapes" viewBox="0 0 1000 572" width="1000" height="572" aria-hidden="true">
      <rect x="0" y="472" width="1000" height="100" fill="var(--band-grey)"/>
      <polygon points="0,0 92,0 0,118" fill="var(--accent-yellow)"/>
      <line x1="100" y1="0" x2="0" y2="128" stroke="var(--rule-white)" stroke-width="6"/>
      <polygon points="810,0 1000,0 1000,30 840,22" fill="var(--accent-yellow)"/>
      <line x1="838" y1="26" x2="1000" y2="36" stroke="var(--rule-white)" stroke-width="5"/>
      <polygon points="1000,170 1000,572 846,572 916,170" fill="var(--accent-red)"/>
      <line x1="902" y1="170" x2="832" y2="572" stroke="var(--rule-white)" stroke-width="6"/>
    </svg>

    <h1 class="brand-title">HOLLER BOOTSTRAP OUTFITTERS</h1>

    <div class="brand-mark">
      <span class="brand-mark-dot"></span>
      <span class="brand-mark-name">HOLLER BOOTSTRAP</span>
    </div>

    <p class="website">www.hollerbootstrap.example</p>

    <p class="motto">My motto "DONT judge how we look...Judge the WILD mess we make!!</p>
  </article>
</body>
</html>
```